Word template Letterhead for Australian Law Firm

We are a small law firm based in Manly, NSW, Australia. We have had a new logo designed for us and wish to freshen up the appearance of our letterhead. We require the letterhead to be in a word document that we can type over. This will not be a ‘printed’ letterhead because we send the majority of our correspondence via email. We would like to see a few options. We have attached our previous letterhead as well as the artwork for our new logo. We like the idea of a watermark across the bottom of the letter but the watermark must stay in place and we must be able to type over it. We are open to some colour throughout the letterhead because the majority of our correspondence is sent electronically. We also use electronic signatures. I have uploaded an example of this.The letterhead must include:-1. Our address details – including our phone number, physical address, website address etc. These details can be found on the copy of our previous letterhead;2. ABN Number;3. The words ‘Brevicor (NSW) Pty Ltd ACN 482 731 058 trading as Shipton & AssociatesLiability limited by a scheme approved under Professional Standards Legislation. The letterhead does not need to include the names and qualifications of the people working at the firm. Thank you.

Target Market(s)

Clients and other parties

Industry/Entity Type

Law Firm

Font styles to use
Other font styles liked:
• raleway, montserrat

Colors

Designer to choose colors to be used in the design.

Requirements
Must have
• Certain wording - please see project description.
• Must be a word document and must be able to type over the watermark etc.
Nice to have
• Watermark at the bottom of the letter.

```html
<!DOCTYPE html>
<html lang="en">
<head>
<meta charset="utf-8">
<title>Kervell &amp; Associates Letterhead</title>
<link href="https://fonts.googleapis.com/css2?family=Montserrat:ital,wght@0,400;0,500;0,700;1,400&display=swap" rel="stylesheet">
<style>
  :root {
    --ink: #1e1e1e;
    --brand: #3f4d96;
    --rule: #8a8a8a;
    --sig-line: #d9d9d9;
    --sig-fill: #f4f4f6;
    --badge: #2a2a2a;
    --paper: #ffffff;
  }
  * { margin: 0; padding: 0; box-sizing: border-box; }
  html, body { width: 849px; height: 1200px; overflow: hidden; background: var(--paper); }
  body { font-family: "Montserrat", sans-serif; color: var(--ink); }
  .letterhead { position: relative; width: 849px; height: 1200px; }

  .brand-mark {
    position: absolute; left: 101px; top: 144px;
    display: flex; align-items: center; gap: 8px;
  }
  .brand-dot { width: 12px; height: 12px; border-radius: 50%; background: var(--brand); }
  .brand-name { font-size: 11px; font-weight: 700; letter-spacing: 1px; color: var(--brand); }

  .contact {
    position: absolute; left: 492px; top: 84px;
    border-left: 1px solid var(--rule);
    padding-left: 9px;
    font-size: 11.6px; line-height: 17.7px; font-style: normal;
  }
  .contact b { font-weight: 700; }

  .salutation { position: absolute; left: 101px; top: 300px; font-size: 14px; }

  .body-copy {
    position: absolute; left: 101px; top: 355px; width: 670px;
    font-size: 14px; line-height: 23.05px; white-space: nowrap;
  }
  .body-copy p + p { margin-top: 23.05px; }

  .sign-off { position: absolute; left: 101px; top: 912px; font-size: 14px; font-style: italic; }
  .signature {
    position: absolute; left: 101px; top: 943px; width: 153px; height: 55px;
    border-right: 1px solid var(--sig-line); border-bottom: 1px solid var(--sig-line);
    background: linear-gradient(90deg, var(--sig-fill), var(--paper));
  }
  .signatory { position: absolute; left: 101px; top: 1007px; font-size: 14px; font-weight: 500; }

  .legal {
    position: absolute; left: 102px; top: 1138px;
    font-size: 11.4px; line-height: 14px;
  }
  .accreditation {
    position: absolute; left: 714px; top: 1119px; width: 61px; height: 61px;
    border-radius: 50%; border: 2px solid var(--badge);
  }
</style>
</head>
<body>
<main class="letterhead">
  <header>
    <div class="brand-mark">
      <span class="brand-dot"></span>
      <span class="brand-name">Kervell &amp; Associates</span>
    </div>
    <address class="contact">
      SUITE 4, 12 CORAL PARADE | KELBY NSW 2093<br>
      <b>T</b> (02) 9000 4218 | <b>F</b> (02) 9000 4219<br>
      <b>M</b> reception@brevicorlaw.com.au<br>
      www.kervellandassociates.com.au<br>
      ABN: 48 482 731 058
    </address>
  </header>

  <p class="salutation">Dear Sir/Madam</p>

  <section class="body-copy">
    <p>Lorem ipsum dolor sit amet, consectetuer adipiscing elit, sed diam nonummy nibh euismod<br>
    tincidunt ut laoreet dolore magna aliquam erat volutpat. Ut wisi enim ad minim veniam,<br>
    quis nostrud exerci tation ullamcorper suscipit lobortis nisl ut aliquip ex ea commodo conse-<br>
    quat. Duis autem vel eum iriure dolor in hendrerit in vulputate velit esse molestie consequat,<br>
    vel illum dolore eu feugiat nulla facilisis at vero eros et accumsan et iusto odio dignissim qui<br>
    blandit praesent luptatum zzril delenit augue duis dolore te feugait nulla facilisi.<br>
    Lorem ipsum dolor sit amet, cons ectetuer adipiscing elit, sed diam nonummy nibh euis-<br>
    mod tincidunt ut laoreet dolore magna aliquam erat volutpat. Ut wisi enim ad minim<br>
    veniam, quis nostrud exerci tation ullamcorper suscipit lobortis nisl ut aliquip ex ea commo-<br>
    do consequat.</p>
    <p>Lorem ipsum dolor sit amet, consectetuer adipiscing elit, sed diam nonummy nibh euismod<br>
    tincidunt ut laoreet dolore magna aliquam erat volutpat. Ut wisi enim ad minim veniam,<br>
    quis nostrud exerci tation ullamcorper suscipit lobortis nisl ut aliquip ex ea commodo conse-<br>
    quat. Duis autem vel eum iriure dolor in hendrerit in vulputate velit esse molestie consequat,<br>
    vel illum dolore eu feugiat nulla facilisis at vero eros et accumsan et iusto odio dignissim qui<br>
    blandit praesent luptatum zzril delenit augue duis dolore te feugait nulla facilisi.<br>
    Lorem ipsum dolor sit amet, cons ectetuer adipiscing elit, sed diam nonummy nibh euis-<br>
    mod tincidunt ut laoreet dolore magna aliquam erat volutpat. Ut wisi enim ad minim<br>
    veniam, quis nostrud exerci tation ullamcorper suscipit lobortis nisl ut aliquip ex ea commo-<br>
    do consequat.</p>
  </section>

  <p class="sign-off">Yours faithfully,</p>
  <div class="signature" role="img" aria-label="Handwritten electronic signature"></div>
  <p class="signatory">Hannah Morrow</p>

  <footer>
    <p class="legal">Brevicor (NSW) Pty Ltd ACN 482 731 058 trading as Kervell &amp; Associates<br>
    Liability limited by a scheme approved under Professional Standards Legislation</p>
    <div class="accreditation" role="img" aria-label="Accreditation badge"></div>
  </footer>
</main>
</body>
</html>
```